TKR Advisory Business Cards

Hi there,

I'd like to make a simple new business card design with the logo we already have created for our business.

I need a double sided business card with our logo on the front side and the company and person's details on the back side.

I'd like it to be on a white background and no background so I can potentially use it with either white paper or put it on different coloured paper in accordance with our business colours.

Please use the logo images I have attached and also the fonts.

So Front side:
- Logo in centre of business card (use medium logo so there is a pretty decent border around it, so don't want to fill the whole card but to make it prominent).

Back Side.
- We need 3 different business cards with the different people's name on each.

ie.

Dorian Halvreck
Business Development Manager

m +61 437 206 518
e dorian@tkradvisory.com.au
w tkradvisory.com.au

- Also I'd like to put only the cog/power button logo in the top right hand corner of the card.
(You might need to chop the current logo in half as I don't have a seperate log just for this)
- Also I'd like some lines running on the top left hand corner diagonally, anything that will add to the design or some swirling lines that add some cool effect to the card.

Also I'd like to maybe put our ABN in the bottom right hand corner of the card in a smaller font.

I'd like to also talk to the designer if possible so I can get my idea across a bit better.

Thanks!

Regards,
Dorian

```html
<!DOCTYPE html>
<html lang="en">
<head>
<meta charset="utf-8">
<title>TKR Advisory Business Cards</title>
<link href="https://fonts.googleapis.com/css2?family=Lato:wght@400;700&display=swap" rel="stylesheet">
<style>
  :root {
    --stage: #1d1d1d;
    --paper: #ffffff;
    --ink: #2b2b2b;
    --charcoal: #4a4a4a;
    --edge: #5a5a5a;
    --orange: #f7941d;
    --orange-light: #fbb040;
    --orange-deep: #f58220;
  }
  * { margin: 0; padding: 0; box-sizing: border-box; }
  html, body {
    width: 1200px;
    height: 926px;
    overflow: hidden;
    background: var(--stage);
    font-family: "Lato", sans-serif;
  }
  .sheet {
    position: relative;
    width: 1200px;
    height: 926px;
    display: flex;
    align-items: center;
    justify-content: center;
    gap: 40px;
  }
  .card {
    position: relative;
    width: 540px;
    height: 330px;
    background: var(--paper);
    overflow: hidden;
  }

  /* Front side */
  .card--front {
    border: 10px solid var(--edge);
  }
  .card--front .frame {
    position: absolute;
    inset: 8px;
    border: 3px solid var(--orange);
  }
  .brand {
    display: flex;
    align-items: center;
    gap: 12px;
    white-space: nowrap;
  }
  .brand__dot {
    border-radius: 50%;
    background: var(--orange);
    flex: none;
  }
  .brand__name {
    color: var(--charcoal);
    font-weight: 700;
    line-height: 1;
  }
  .card--front .brand {
    position: absolute;
    left: 50%;
    top: 50%;
    transform: translate(-50%, -50%);
  }
  .card--front .brand__dot { width: 44px; height: 44px; }
  .card--front .brand__name { font-size: 42px; }

  /* Back side */
  .card--back .brand {
    position: absolute;
    left: 26px;
    top: 30px;
  }
  .card--back .brand__dot { width: 28px; height: 28px; }
  .card--back .brand__name { font-size: 26px; }

  .person {
    position: absolute;
    right: 28px;
    top: 78px;
    text-align: right;
    color: var(--ink);
    white-space: nowrap;
  }
  .person__name {
    font-size: 22px;
    font-weight: 400;
    letter-spacing: 0.3px;
  }
  .person__role {
    font-size: 12.5px;
    margin-top: 4px;
  }
  .contacts {
    position: absolute;
    left: 30px;
    top: 128px;
    list-style: none;
    color: var(--ink);
    font-size: 14px;
    line-height: 1.55;
    white-space: nowrap;
  }
  .contacts b {
    display: inline-block;
    width: 20px;
    font-weight: 700;
  }
  .swoosh {
    position: absolute;
    left: 0;
    bottom: 0;
    width: 540px;
    height: 118px;
  }
  .emblem {
    position: absolute;
    right: -22px;
    bottom: -44px;
    width: 200px;
    height: 200px;
    border-radius: 50%;
    background: var(--charcoal);
    border: 6px solid var(--paper);
  }
</style>
</head>
<body>
<main class="sheet">

  <section class="card card--front" aria-label="Card front">
    <div class="frame"></div>
    <div class="brand">
      <span class="brand__dot"></span>
      <span class="brand__name">TKR Advisory</span>
    </div>
  </section>

  <section class="card card--back" aria-label="Card back">
    <svg class="swoosh" viewBox="0 0 540 118" preserveAspectRatio="none" aria-hidden="true">
      <defs>
        <linearGradient id="band" x1="0" y1="0" x2="1" y2="1">
          <stop offset="0" stop-color="#fbb040"/>
          <stop offset="1" stop-color="#f58220"/>
        </linearGradient>
      </defs>
      <path d="M0 6 C140 0 290 40 540 112 L540 118 L0 118 Z" fill="url(#band)"/>
      <path d="M0 34 C160 24 320 64 540 118 L0 118 Z" fill="#f7941d" opacity="0.85"/>
      <path d="M0 14 C150 6 300 44 520 110" fill="none" stroke="#ffffff" stroke-width="2" opacity="0.7"/>
      <path d="M0 22 C170 16 320 54 540 114" fill="none" stroke="#ffffff" stroke-width="1" opacity="0.5"/>
      <path d="M0 70 C190 64 340 92 540 118 L0 118 Z" fill="#f58220" opacity="0.6"/>
    </svg>

    <div class="emblem" role="img" aria-label="Large brand emblem area"></div>

    <div class="brand">
      <span class="brand__dot"></span>
      <span class="brand__name">TKR Advisory</span>
    </div>

    <div class="person">
      <p class="person__name">Dorian Halvreck</p>
      <p class="person__role">Business Development Manager</p>
    </div>

    <ul class="contacts">
      <li><b>m</b>: +61 437 206 518</li>
      <li><b>e</b>: dorian@tkradvisory.com.au</li>
      <li><b>w</b>: tkradvisory.com.au</li>
    </ul>
  </section>

</main>
</body>
</html>
```